HARD MONEY ORIGINATOR RECRUITMENT.
Looking for individuals to help us originate loans for real estate investor financing primarily used to fix up properties and resell.
HARD MONEY ORIGINATORS WANTED
No Licensing Required
Work As Independent Contractor
1% Flat Finders Fee on Each Loan
Referral Compensation for Recruiting New Originators
Immediate Payouts
Programs Offered Nationwide
Marketing Assistance and Support Available
Email mpelton@brightquaylending.com for more information or call (800) 641-2950 Ext. 24 Brightquay Lending Services, Inc. www.brightquaylending.com NMLS #318760
Industry/Entity Type
Real Estate
Look and feel
Each slider illustrates characteristics of the customer's brand and the style your logo design should communicate.

```html
<!DOCTYPE html>
<html lang="en">
<head>
<meta charset="utf-8">
<title>Hard Money Originators Wanted – Brightquay Lending Services</title>
<link rel="stylesheet" href="https://fonts.googleapis.com/css2?family=Arvo:wght@700&family=Lato:wght@300;400;700&display=swap">
<style>
  :root {
    --page-bg: #e9e7e3;
    --paper: #ffffff;
    --ink: #1c1c1c;
    --ink-soft: #3a3a3a;
    --brand-blue: #2160d8;
    --photo-warm: #c9b79a;
    --photo-wood: #9c7b58;
    --photo-blue: #5d7fa8;
    --photo-plaid: #7a3a4a;
  }
  * { box-sizing: border-box; margin: 0; padding: 0; }
  html, body { width: 1200px; height: 1200px; overflow: hidden; }
  body { background: var(--page-bg); font-family: "Lato", sans-serif; color: var(--ink); }

  .flyer {
    position: absolute; left: 160px; top: 30px;
    width: 880px; height: 1140px;
    background: var(--paper);
    box-shadow: 0 6px 24px rgba(0,0,0,0.18);
    overflow: hidden;
  }
  .photo-layer { position: absolute; left: 0; top: 0; width: 880px; height: 860px; }

  .brand {
    position: absolute; left: 450px; top: 120px; width: 400px;
    display: flex; align-items: center; justify-content: center; gap: 14px;
  }
  .brand-dot { width: 34px; height: 34px; border-radius: 50%; background: var(--brand-blue); flex: none; }
  .brand-name { font-family: "Lato", sans-serif; font-weight: 700; font-size: 26px; color: var(--brand-blue); line-height: 1.15; }

  .headline {
    position: absolute; left: 440px; top: 285px; width: 420px;
    font-family: "Arvo", serif; font-weight: 700; text-align: center; line-height: 1;
  }
  .headline .line { display: block; color: var(--ink); font-size: 46px; letter-spacing: 1px; }
  .headline .wanted { display: block; color: var(--brand-blue); font-size: 76px; margin-top: 8px; letter-spacing: 1px; }

  .benefits {
    position: absolute; left: 110px; top: 830px;
    list-style: none; font-weight: 300; font-size: 22px; line-height: 28px; color: var(--ink-soft);
  }
  .benefits li::before { content: "\2713"; margin-right: 10px; font-weight: 400; }

  .footer {
    position: absolute; left: 110px; top: 1040px; right: 40px;
    display: flex; align-items: center; gap: 24px; font-size: 18px; color: var(--ink-soft);
  }
  .footer .divider { width: 4px; height: 52px; background: var(--ink); flex: none; }
  .company { font-weight: 400; line-height: 1.2; width: 190px; }
  .contact-title { font-weight: 700; font-size: 19px; color: var(--ink); }
  .contact-row { display: flex; align-items: center; gap: 6px; font-size: 16px; line-height: 1.3; }
  .contact-row.phone { color: var(--brand-blue); }
  .web { text-align: center; font-size: 17px; line-height: 1.3; }
  .web svg { display: block; margin: 0 auto 2px; }
</style>
</head>
<body>
  <main class="flyer">
    <svg class="photo-layer" viewBox="0 0 880 860">
      <defs>
        <linearGradient id="grad-office" x1="0" y1="0" x2="1" y2="1">
          <stop offset="0" stop-color="#ece6da"/>
          <stop offset="1" stop-color="#9c7b58"/>
        </linearGradient>
        <linearGradient id="grad-workshop" x1="0" y1="0" x2="1" y2="1">
          <stop offset="0" stop-color="#c9b79a"/>
          <stop offset="1" stop-color="#5d7fa8"/>
        </linearGradient>
        <linearGradient id="grad-builder" x1="0" y1="0" x2="0" y2="1">
          <stop offset="0" stop-color="#d8d2c6"/>
          <stop offset="1" stop-color="#7a3a4a"/>
        </linearGradient>
      </defs>
      <polygon class="photo-office" role="img" aria-label="Photo: contractor in hard hat reviewing plans with a client in a renovated kitchen"
        points="0,70 300,70 400,245 300,420 0,420" fill="url(#grad-office)"/>
      <rect class="accent-block" x="90" y="560" width="170" height="190" fill="var(--brand-blue)"/>
      <polygon class="photo-workshop" role="img" aria-label="Photo: worker in hard hat cutting lumber with a power saw"
        points="340,510 490,510 550,645 490,780 340,780 280,645" fill="url(#grad-workshop)"/>
      <polygon class="photo-builder" role="img" aria-label="Photo: smiling builder in hard hat carrying lumber on his shoulder"
        points="620,490 880,490 880,745 750,815 610,745 565,625" fill="url(#grad-builder)"/>
    </svg>

    <div class="brand">
      <span class="brand-dot"></span>
      <span class="brand-name">Brightquay Lending Services, Inc.</span>
    </div>

    <h1 class="headline">
      <span class="line">HARD MONEY</span>
      <span class="line">ORIGINATORS</span>
      <span class="wanted">WANTED</span>
    </h1>

    <ul class="benefits">
      <li>No Licensing Required</li>
      <li>Work As Independent Contractor</li>
      <li>1% Flat Finders Fee on Each Loan</li>
      <li>Referral Compensation for Recruiting New Originators</li>
      <li>Immediate Payouts</li>
      <li>Programs Offered Nationwide</li>
      <li>Marketing Assistance and Support Available</li>
    </ul>

    <footer class="footer">
      <div class="company">Brightquay Lending Services, Inc.</div>
      <span class="divider"></span>
      <div class="contact">
        <div class="contact-title">CONTACT US</div>
        <div class="contact-row email">
          <svg width="14" height="11" viewBox="0 0 14 11"><rect x="0.75" y="0.75" width="12.5" height="9.5" fill="none" stroke="currentColor" stroke-width="1.5"/><path d="M1 1 L7 6 L13 1" fill="none" stroke="currentColor" stroke-width="1.5"/></svg>
          mpelton@brightquaylending.com
        </div>
        <div class="contact-row phone">
          <svg width="13" height="13" viewBox="0 0 24 24"><path fill="var(--ink)" d="M6.6 10.8a15.1 15.1 0 0 0 6.6 6.6l2.2-2.2a1 1 0 0 1 1-.25 11.4 11.4 0 0 0 3.6.57 1 1 0 0 1 1 1V20a1 1 0 0 1-1 1A17 17 0 0 1 3 4a1 1 0 0 1 1-1h3.5a1 1 0 0 1 1 1c0 1.25.2 2.45.57 3.57a1 1 0 0 1-.25 1z"/></svg>
          (800) 641-2950 Ext. 24
        </div>
      </div>
      <span class="divider"></span>
      <div class="web">
        <svg width="34" height="24" viewBox="0 0 34 24"><rect x="6" y="2" width="22" height="15" rx="1.5" fill="none" stroke="var(--ink)" stroke-width="2.2"/><rect x="1" y="19" width="32" height="3" rx="1" fill="var(--ink)"/></svg>
        www.brightquaylending.com<br>NMLS #318760
      </div>
    </footer>
  </main>
</body>
</html>
```